Here is the link where the current banner is featured https://www.brimkit.com.au/collections/gel-blasters

I need the banner recreated into desktop and mobile format size.
Update the key points to:
- FREE SHIPPING AUSTRALIA WIDE
- SAME DAY DISPATCH
- BEST PRICE GUARANTEE
- 3000+ 5 STAR REVIEWS
- BEST SERVICE & WARRANTY
- 100% SECURE CHECKOUT

I want the banner to suit the style of the website and make it look better than the last graphic.

I also need the "save even more" picture to be recreated as it looks very plain at the moment,

```html
<!DOCTYPE html>
<html lang="en">
<head>
<meta charset="utf-8">
<title>Brimkit – Gel Blasters Benefits Banner</title>
<link href="https://fonts.googleapis.com/css2?family=Montserrat:wght@500;600&display=swap" rel="stylesheet">
<style>
  :root {
    --page: #ffffff;
    --charcoal: #232323;
    --red-bright: #e0161e;
    --red-light: #c31a20;
    --red-mid: #a8141a;
    --red-dark: #7a0b10;
    --paper: #f2f2f2;
    --ink: #ffffff;
  }
  * { box-sizing: border-box; margin: 0; padding: 0; }
  html, body {
    width: 1200px; height: 555px; overflow: hidden;
    background: var(--page);
  }
  .banner {
    position: relative; width: 1200px; height: 555px;
    font-family: "Montserrat", sans-serif;
  }
  .banner__art { position: absolute; inset: 0; }
  .benefits {
    position: absolute; top: 240px; left: 0; width: 1200px;
    list-style: none;
  }
  .benefit {
    position: absolute; top: 0; width: 150px; margin-left: -75px;
    text-align: center; color: var(--ink);
  }
  .benefit__icon { display: block; width: 58px; height: 58px; margin: 0 auto 20px; }
  .benefit__label {
    font-size: 14px; font-weight: 500; line-height: 18px;
    letter-spacing: 0.2px; text-transform: uppercase; white-space: nowrap;
  }
</style>
</head>
<body>
<main class="banner">
  <svg class="banner__art" width="1200" height="555" viewBox="0 0 1200 555">
    <defs>
      <radialGradient id="burst" cx="600" cy="275" r="600" gradientUnits="userSpaceOnUse">
        <stop offset="0" stop-color="var(--red-light)"/>
        <stop offset="0.5" stop-color="var(--red-mid)"/>
        <stop offset="1" stop-color="var(--red-dark)"/>
      </radialGradient>
    </defs>
    <rect class="panel" x="13" y="48" width="1174" height="462" fill="var(--charcoal)"/>
    <polygon class="tear tear--top" fill="var(--paper)"
      points="13,162 70,158 130,161 190,154 260,156 330,149 400,151 470,143 540,145 610,137 680,139 750,131 820,130 890,124 960,121 1030,115 1100,112 1150,106 1187,103 1187,124 13,178"/>
    <polygon class="band" role="img" aria-label="Red sunburst band with halftone dot texture" fill="url(#burst)"
      points="13,172 90,170 170,166 250,164 330,159 410,157 490,152 570,150 650,145 730,142 810,138 890,134 970,131 1050,127 1130,124 1187,121 1187,398 1120,396 1050,394 980,392 900,391 820,393 740,397 660,400 580,402 500,403 420,404 340,405 260,405 180,405 100,404 13,404"/>
    <polygon class="tear tear--bottom" fill="var(--paper)"
      points="13,402 100,402 180,403 260,403 340,403 420,402 500,401 580,400 660,398 740,395 820,391 900,389 980,390 1050,392 1120,394 1187,396 1187,409 1140,408 1080,405 1020,404 960,402 900,400 840,402 780,404 720,408 660,410 600,412 540,416 480,420 420,424 360,426 300,429 240,431 180,433 120,434 60,435 13,436"/>
    <g class="cart-tag" stroke="var(--paper)" fill="none">
      <path d="M1116,121 Q1120,160 1131,176" stroke-width="1"/>
      <circle cx="1131" cy="201" r="26" fill="var(--ink)" stroke="none"/>
      <g stroke="var(--red-mid)" stroke-width="2.4" stroke-linecap="round" stroke-linejoin="round">
        <path d="M1116,189 h5 l4,16 h16 l3,-11 h-21"/>
        <circle cx="1127" cy="211" r="1.8" fill="var(--red-mid)"/>
        <circle cx="1139" cy="211" r="1.8" fill="var(--red-mid)"/>
      </g>
    </g>
    <g class="blaster-silhouettes" fill="var(--ink)">
      <rect role="img" aria-label="White silhouette of a submachine-style gel blaster" x="350" y="374" width="150" height="86" rx="14"/>
      <rect role="img" aria-label="White silhouette of a rifle-style gel blaster" x="518" y="364" width="96" height="110" rx="14"/>
      <rect role="img" aria-label="White silhouette of a pistol gel blaster with light" x="630" y="376" width="106" height="90" rx="14"/>
      <rect role="img" aria-label="White silhouette of an assault-style gel blaster" x="756" y="368" width="116" height="102" rx="14"/>
    </g>
  </svg>

  <ul class="benefits">
    <li class="benefit" style="left:217px">
      <svg class="benefit__icon" viewBox="0 0 60 60" fill="none" stroke="#fff" stroke-width="3" stroke-linecap="round">
        <circle cx="34" cy="33" r="20"/><path d="M30 10h8M34 10v3M48 16l3-3"/>
        <path d="M34 33V21M34 33l8 5"/><path d="M4 26h9M2 33h10M6 40h8"/>
      </svg>
      <p class="benefit__label">Free Shipping<br>Australia Wide</p>
    </li>
    <li class="benefit" style="left:365px">
      <svg class="benefit__icon" viewBox="0 0 60 60" fill="none" stroke="#fff" stroke-width="3" stroke-linecap="round">
        <rect x="4" y="9" width="40" height="38" rx="3"/><path d="M4 19h40M13 4v9M35 4v9"/>
        <path d="M11 26h4M19 26h4M27 26h4M11 33h4M19 33h4M11 40h4" stroke-width="2.5"/>
        <circle cx="44" cy="44" r="13" fill="#a8141a"/>
        <text x="44" y="49" font-family="Montserrat, sans-serif" font-size="12" font-weight="600" fill="#fff" stroke="none" text-anchor="middle">24</text>
      </svg>
      <p class="benefit__label">Same Day<br>Dispatch</p>
    </li>
    <li class="benefit" style="left:514px">
      <svg class="benefit__icon" viewBox="0 0 60 60" fill="none" stroke="#fff" stroke-width="3" stroke-linejoin="round">
        <circle cx="30" cy="24" r="20"/><circle cx="30" cy="24" r="13"/>
        <path d="M18 40l-6 16 8-4 4 6 5-14M42 40l6 16-8-4-4 6-5-14"/>
        <text x="30" y="30" font-family="Montserrat, sans-serif" font-size="16" font-weight="600" fill="#fff" stroke="none" text-anchor="middle">$</text>
      </svg>
      <p class="benefit__label">Best Price<br>Guarantee</p>
    </li>
    <li class="benefit" style="left:661px">
      <svg class="benefit__icon" viewBox="0 0 60 60" fill="none" stroke="#fff" stroke-width="3">
        <circle cx="30" cy="30" r="26"/><path d="M6 40h48" stroke-width="10"/>
        <text x="30" y="32" font-family="Montserrat, sans-serif" font-size="24" font-weight="600" fill="#fff" stroke="none" text-anchor="middle">5</text>
        <text x="30" y="43" font-family="Montserrat, sans-serif" font-size="8" fill="#a8141a" stroke="none" text-anchor="middle">★★★★★</text>
      </svg>
      <p class="benefit__label">3000+ 5 Star<br>Reviews</p>
    </li>
    <li class="benefit" style="left:810px">
      <svg class="benefit__icon" viewBox="0 0 60 60" fill="none" stroke="#fff" stroke-width="3" stroke-linecap="round">
        <circle cx="30" cy="32" r="24"/>
        <path d="M12 10l34 34M10 14l6-6"/><path d="M48 10l-30 30"/><circle cx="15" cy="45" r="5"/><path d="M44 6a6 6 0 1 0 10 10"/>
      </svg>
      <p class="benefit__label">Best Service &amp;<br>Warranty</p>
    </li>
    <li class="benefit" style="left:958px">
      <svg class="benefit__icon" viewBox="0 0 60 60" fill="none" stroke="#fff" stroke-width="3" stroke-linejoin="round">
        <path d="M30 4l22 8v16c0 14-10 24-22 28C18 52 8 42 8 28V12z"/>
        <rect x="21" y="28" width="18" height="14" rx="2" fill="#fff"/><path d="M24 28v-5a6 6 0 0 1 12 0v5"/>
      </svg>
      <p class="benefit__label">100% Secure<br>Checkout</p>
    </li>
  </ul>
</main>
</body>
</html>
```